Face cream packaging | Cosmetic start-up

This project is about creating design proposals for two different types of packaging. Once to a cream jar made of glass and once to a jar made of plastic.
Three different designs must be created for each type of jar. Later, the different packaging will be used as customization options in an online store for cosmetics.

- The packaging variant made of glass should have color gradients. Three different shades are to be chosen. (Preferably with the primary colors red, blue and green). Note: The designer can create other proposals at will if he has better ideas. The logo must be included in some form. (Link to manufacturer description: https://catalogue.valdorpackaging.com/en/portals/valdorpackaging/assets/12667188/lou-50-ml/)

- With the plastic type of packaging, the designer has a lot of freedom to design. The only requirement is that the design must be artistic. It doesn't matter whether abstract patterns, geometric figures, mandalas or just a basic color is chosen. The main thing is that the packaging inspires. The logo must be included in some form. (Link to manufacturer description: https://catalogue.valdorpackaging.com/en/portals/valdorpackaging/assets/12667181/edda-50-ml/)

Thank you in advance for your work and best regards
Olaf

Target Market(s)

Young people with an affinity for social media and the web. Focus is on the female clientele.

Industry/Entity Type

Cosmetics

Font styles to use
Script

Colors
eea4c8
f59195
85cae6
cadf82

Requirements
Must have
• The logo must be included in some form. (PNG-File attached)
Nice to have
• Other types of packaging (can shape, packaging material)

```html
<!DOCTYPE html>
<html lang="en">
<head>
<meta charset="utf-8">
<title>Bloom Note – Face Cream Label</title>
<link rel="stylesheet" href="https://fonts.googleapis.com/css2?family=Poppins:wght@300;400;500&display=swap">
<style>
  :root {
    --paper: #ffffff;
    --ink: #2b2b2b;
    --ink-soft: #6d6d6d;
    --rule: #8a8a8a;
    --ring: #c7373f;
    --petal-red: #c7373f;
    --petal-rose: #f08a8f;
    --petal-blush: #fbe3e4;
    --petal-sky: #85cae6;
    --petal-lime: #cadf82;
  }
  * { margin: 0; padding: 0; box-sizing: border-box; }
  html, body {
    width: 1200px;
    height: 1200px;
    overflow: hidden;
    background: var(--paper);
  }
  .canvas {
    position: relative;
    width: 1200px;
    height: 1200px;
    display: flex;
    align-items: center;
    justify-content: center;
  }
  .label {
    position: relative;
    width: 1080px;
    height: 440px;
    background: var(--paper);
    overflow: hidden;
  }
  .floral-pattern {
    position: absolute;
    inset: 0;
    background:
      radial-gradient(circle at 8% 70%, rgba(133,202,230,0.55) 0, rgba(133,202,230,0) 22%),
      radial-gradient(circle at 92% 45%, rgba(133,202,230,0.55) 0, rgba(133,202,230,0) 20%),
      radial-gradient(circle at 3% 10%, rgba(202,223,130,0.5) 0, rgba(202,223,130,0) 14%),
      radial-gradient(circle at 26% 30%, rgba(240,138,143,0.85) 0, rgba(240,138,143,0) 24%),
      radial-gradient(circle at 62% 20%, rgba(199,55,63,0.75) 0, rgba(199,55,63,0) 20%),
      radial-gradient(circle at 72% 80%, rgba(240,138,143,0.85) 0, rgba(240,138,143,0) 24%),
      radial-gradient(circle at 40% 95%, rgba(199,55,63,0.7) 0, rgba(199,55,63,0) 18%),
      radial-gradient(circle at 85% 12%, rgba(240,138,143,0.7) 0, rgba(240,138,143,0) 14%),
      linear-gradient(90deg, var(--petal-blush), #fff5f5 50%, var(--petal-blush));
  }
  .seal {
    position: absolute;
    left: 50%;
    top: 50%;
    width: 360px;
    height: 360px;
    transform: translate(-50%, -50%);
    border-radius: 50%;
    background: var(--paper);
    border: 9px solid var(--ring);
    display: flex;
    flex-direction: column;
    align-items: center;
  }
  .brand {
    margin-top: 88px;
    display: flex;
    flex-direction: column;
    align-items: flex-start;
    width: 250px;
  }
  .brand-name {
    font-family: "Poppins", sans-serif;
    font-weight: 300;
    font-size: 40px;
    line-height: 1;
    color: var(--ink-soft);
    letter-spacing: 0.5px;
  }
  .brand-rule {
    margin-top: 34px;
    width: 220px;
    height: 1.5px;
    background: var(--rule);
    align-self: flex-end;
  }
  .product {
    margin-top: auto;
    margin-bottom: 28px;
    text-align: center;
    font-family: "Poppins", sans-serif;
    color: var(--ink);
  }
  .product-type {
    font-size: 15px;
    font-weight: 400;
    letter-spacing: 5px;
  }
  .product-volume {
    margin-top: 4px;
    font-size: 26px;
    font-weight: 500;
  }
</style>
</head>
<body>
  <main class="canvas">
    <section class="label">
      <div class="floral-pattern" role="img" aria-label="Pattern of stylised daisy flowers in red, rose pink, sky blue and lime outlines on white"></div>
      <div class="seal">
        <div class="brand">
          <span class="brand-name">Bloom Note</span>
          <span class="brand-rule"></span>
        </div>
        <div class="product">
          <p class="product-type">FACE CREAM</p>
          <p class="product-volume">50ml</p>
        </div>
      </div>
    </section>
  </main>
</body>
</html>
```